Door Hanger Design for Electricians Serving Homes

I would like our logo incorporated into the door hanger. We would like a place for a tear off section on the bottom of the hanger with our contact information: K&T Electric - (555) 318-6470 - www.kandtelectric.example - info@kandtelectric.example.
Door Hanger Script
Front Side of the Door Hanger:
[Company Logo]
Need a Reliable Electrician?
Your Local Electrical Expert is Just Around the Corner!
• Quick Response Times
• Affordable Rates
• Quality Workmanship
• Fully Licensed & Insured
• Special Offer:
• 10% OFF Your First Service Call!
Back Side of the Door Hanger:
Don't Let Electrical Issues Keep You in the Dark!
From flickering lights to complete system upgrades, we've got all your
residential electrical needs covered. Our services include:
• Electrical Repairs & Troubleshooting
• Lighting Installation & Upgrades
• Safety Inspections & Code Compliance
• Energy-Efficient Solutions
• 24/7 Emergency Services
• Why Choose Us?
• Friendly, Local Service
• Over 30 Years of Experience
• Satisfaction Guaranteed
• Upfront Pricing
Call Us Today: [Your Phone Number]
Visit Our Website: [Your Website]
Book Your Appointment Now and Claim Your 10% Discount!
Offer valid for new customers on the first visit only. Mention this door hanger when
booking.
[Your Company Name and Contact Information]
Follow Us on Social Media for More Tips and Special Offers!
[Icons for social media platforms: Chatterbook, Snapwave, Peeper, etc.]
Design Tips:
Use bold, clear fonts for easy reading.
Incorporate your brand colors and logo for instant recognition.
Include a clear call to action (CTA) on both sides.
Add a tear-off section at the bottom with your contact information for
convenience.
Use high-quality images or graphics related to electrical work to catch
the eye.
This door hanger design and copy aim to attract residential clients by
highlighting the benefits of your electrical services, special offers, and
how they can easily get in touch with you for their electrical needs.
The door knocker template will have three of the same design on front and three of the same design on the back. This template is from the print shop.

```html
<!DOCTYPE html>
<html lang="en">
<head>
<meta charset="UTF-8">
<title>K&amp;T Electric Door Hangers</title>
<link rel="stylesheet" href="https://fonts.googleapis.com/css2?family=Barlow:wght@400;500;600;700&family=Rubik:wght@700;800;900&display=swap">
<style>
:root{
  --red:#f10d0d;
  --black:#0b0b0b;
  --white:#ffffff;
  --stage:#575757;
  --rule:#6a6a6a;
}
*{margin:0;padding:0;box-sizing:border-box}
html,body{width:1200px;height:1188px;overflow:hidden}
body{background:var(--stage);position:relative;font-family:"Barlow",sans-serif;color:var(--white)}
.hanger{position:absolute;top:59px;width:440px;height:1070px;overflow:hidden;background:var(--white);box-shadow:0 10px 30px rgba(0,0,0,.45)}
.hanger--front{left:130px}
.hanger--back{left:630px}
.hanger svg.shapes{position:absolute;inset:0;width:440px;height:1070px}
.abs{position:absolute}
.logo{font-family:"Barlow",sans-serif;font-weight:700;color:var(--black);line-height:1;white-space:nowrap}
.headline{font-family:"Rubik",sans-serif;font-weight:800;text-align:right;line-height:1;right:26px;white-space:nowrap}
.red{color:var(--red)}
.lead{font-weight:500;text-align:right;right:26px;line-height:1.1}
.list{list-style:none}
.list li{display:flex;align-items:center;gap:10px;border-bottom:1px dashed var(--rule);padding:3px 0 4px;white-space:nowrap}
.bolt{display:inline-block;width:9px;height:15px;background:var(--red);flex:none;clip-path:polygon(55% 0,100% 0,65% 42%,100% 42%,20% 100%,40% 55%,5% 55%)}
.section-title{font-weight:600;color:var(--red)}
.contact{font-weight:500;white-space:nowrap}
.contact b{font-weight:600;color:var(--red)}
.cta-small{font-weight:500;text-align:center;white-space:nowrap}
.cta-big{font-weight:700;color:var(--red);text-align:center;white-space:nowrap}
.pill{background:var(--red);color:var(--white);font-weight:700;border-radius:12px;padding:4px 14px;white-space:nowrap}
.socials{display:flex;gap:10px;align-items:center;font-size:11px;font-weight:600}
.socials span{display:flex;align-items:center;gap:4px}
.socials i{width:9px;height:9px;border-radius:50%;background:var(--red);display:inline-block}
</style>
</head>
<body>

<section class="hanger hanger--front" aria-label="Door hanger front">
  <svg class="shapes" viewBox="0 0 440 1070">
    <defs>
      <linearGradient id="workGlow" x1="0" y1="0" x2="1" y2="1">
        <stop offset="0" stop-color="#c2571f"/>
        <stop offset=".45" stop-color="#3a3030"/>
        <stop offset="1" stop-color="#151515"/>
      </linearGradient>
    </defs>
    <polygon points="0,690 440,0 440,1070 0,1070" fill="#0b0b0b"/>
    <polygon points="95,260 95,190 130,150 210,150 440,20 440,440 154,626 30,664 289,338 120,311" fill="url(#workGlow)" role="img" aria-label="Photo of an electrician in a hard hat working on a wired control panel"/>
    <polygon points="195,150 426,0 440,0 440,20 210,150" fill="#f10d0d"/>
    <polygon points="270,340 289,338 30,664 0,705 0,680" fill="#f10d0d"/>
    <polygon points="120,311 289,338 270,344 110,318" fill="#f10d0d"/>
    <polygon points="154,626 440,440 440,456 120,640" fill="#f10d0d"/>
    <line x1="135" y1="5" x2="210" y2="70" stroke="#0b0b0b" stroke-width="3"/>
    <circle cx="222" cy="95" r="50" fill="#0b0b0b" stroke="#f10d0d" stroke-width="5"/>
    <path d="M440,790 L440,930 L348,926 Q332,924 342,912 Z" fill="#f10d0d"/>
  </svg>

  <div class="abs logo" style="left:30px;top:372px;font-size:28px">K&amp;T Electric</div>

  <div class="abs headline red" style="top:560px;font-size:48px">Need</div>
  <div class="abs headline" style="top:614px;font-size:42px;color:var(--white)">a Reliable</div>
  <div class="abs headline red" style="top:660px;font-size:60px">Electrician?</div>
  <div class="abs lead" style="top:738px;font-size:22px">Your Local Electrical Expert<br>is Just Around the Corner!</div>

  <ul class="abs list" style="left:38px;top:820px;width:165px;font-size:13px;font-weight:500">
    <li><span class="bolt"></span>Quick Response Times</li>
    <li><span class="bolt"></span>Affordable Rates</li>
    <li><span class="bolt"></span>Quality Workmanship</li>
    <li style="border:0"><span class="bolt"></span>Fully Licensed &amp; Insured</li>
  </ul>

  <div class="abs" style="left:233px;top:818px;line-height:1">
    <div style="font-size:18px;font-weight:500">Special Offer:</div>
    <div style="font-family:'Rubik',sans-serif;font-weight:800;font-size:30px;margin-top:8px"><span class="red">10%</span> OFF</div>
    <div style="font-size:13px;font-weight:500;margin-top:4px">Your First Service</div>
    <div class="red" style="font-size:17px;font-weight:600;margin-top:2px">Call!</div>
  </div>

  <div class="abs contact" style="left:36px;top:944px;font-size:16px;line-height:1.35">
    Call Us Today: <b style="font-size:21px">555-318-6470</b><br>
    Visit Our Website: www.kandtelectric.example
  </div>
  <div class="abs cta-small" style="left:0;right:0;top:1006px;font-size:16px">Book Your Appointment Now and</div>
  <div class="abs cta-big" style="left:0;right:0;top:1024px;font-size:28px">Claim Your 10% Discount!</div>
</section>

<section class="hanger hanger--back" aria-label="Door hanger back">
  <svg class="shapes" viewBox="0 0 440 1070">
    <defs>
      <linearGradient id="panelFade" x1="0" y1="0" x2="0" y2="1">
        <stop offset="0" stop-color="#2a2a2a"/>
        <stop offset="1" stop-color="#0d0d0d"/>
      </linearGradient>
    </defs>
    <polygon points="0,300 440,60 440,1070 0,1070" fill="url(#panelFade)" role="img" aria-label="Faint background photo of an electrician at work"/>
    <line x1="160" y1="5" x2="215" y2="72" stroke="#0b0b0b" stroke-width="3"/>
    <circle cx="245" cy="105" r="50" fill="#0b0b0b" stroke="#f10d0d" stroke-width="5"/>
    <path d="M440,720 L440,880 L254,880 Q238,876 250,864 Z" fill="#f10d0d"/>
    <polygon points="440,930 440,1070 330,1070" fill="#f10d0d"/>
  </svg>

  <div class="abs logo" style="left:28px;top:128px;font-size:24px">K&amp;T Electric</div>

  <div class="abs headline red" style="top:212px;font-size:40px">Don't</div>
  <div class="abs headline" style="top:252px;font-size:40px;color:var(--white)">Let Electrical</div>
  <div class="abs headline" style="top:292px;font-size:40px;color:var(--white)">Issues <span class="red">Keep You</span></div>
  <div class="abs headline red" style="top:332px;font-size:40px">in the Dark!</div>
  <div class="abs lead" style="top:388px;font-size:17px;width:360px">From flickering lights to complete system upgrades, we've got all your residential electrical needs covered.</div>

  <div class="abs section-title" style="left:50px;top:470px;font-size:22px">Our Services</div>
  <ul class="abs list" style="left:26px;top:502px;width:340px;font-size:17px;font-weight:500">
    <li><span class="bolt"></span>Electrical Repairs &amp; Troubleshooting</li>
    <li><span class="bolt"></span>Lighting Installation &amp; Upgrades</li>
    <li><span class="bolt"></span>Safety Inspections &amp; Code Compliance</li>
    <li><span class="bolt"></span>Energy-Efficient Solutions</li>
    <li style="border:0"><span class="bolt"></span>24/7 Emergency Services</li>
  </ul>

  <div class="abs section-title" style="left:30px;top:690px;font-size:22px">Why Choose Us?</div>
  <ul class="abs list" style="left:12px;top:722px;width:250px;font-size:17px;font-weight:500">
    <li><span class="bolt"></span>Friendly, Local Service</li>
    <li><span class="bolt"></span>Over 30 Years of Experience</li>
    <li><span class="bolt"></span>Satisfaction Guaranteed</li>
    <li style="border:0"><span class="bolt"></span>Upfront Pricing</li>
  </ul>

  <div class="abs contact" style="left:22px;top:892px;font-size:14px;line-height:1.4">
    Call Us Today: <b style="font-size:19px">555-318-6470</b><br>
    Visit Our Website: www.kandtelectric.example
  </div>
  <div class="abs cta-small" style="left:22px;top:950px;font-size:14px">Book Your Appointment Now and Claim</div>
  <div class="abs pill" style="left:22px;top:972px;font-size:22px">Your 10% Discount!</div>
  <div class="abs" style="left:30px;top:1022px;font-size:12px;font-weight:500;line-height:1.2">Follow Us on Social Media<br>for More Tips and Special Offers!</div>
  <div class="abs socials" style="left:30px;top:1052px">
    <span><i></i>Chatterbook</span><span><i></i>Snapwave</span><span><i></i>Peeper</span>
  </div>
</section>

</body>
</html>
```